Business Card Design
Brightvale Marks
Modern
Kemi Varo
47 Olumide Bankole Crescent
Wuse 2
Abuja
Nigeria
info@brightvalemarks.com
www.brightvalemarks.com

```html
<!DOCTYPE html>
<html lang="en">
<head>
<meta charset="utf-8">
<title>Brightvale Marks — Business Card</title>
<link rel="stylesheet" href="https://fonts.googleapis.com/css2?family=Cinzel:wght@400;700&family=Open+Sans:wght@400;600;700&display=swap">
<style>
  :root {
    --backdrop: #5e3322;
    --card: #050505;
    --brand-blue: #3f8fc6;
    --band-green: #79b83a;
    --band-green-dark: #4f8a22;
    --band-blue: #2aa6dd;
    --band-blue-dark: #14639c;
    --text-light: #ffffff;
    --text-muted: #9fb7cc;
  }
  * { box-sizing: border-box; margin: 0; padding: 0; }
  html, body { width: 1200px; height: 646px; overflow: hidden; }
  body {
    background: var(--backdrop);
    font-family: "Open Sans", Arial, sans-serif;
    position: relative;
  }
  .card {
    position: absolute;
    top: 173px;
    width: 520px;
    height: 300px;
    background: var(--card);
    overflow: hidden;
    box-shadow: 0 8px 24px rgba(0,0,0,.45);
  }
  .card--front { left: 50px; }
  .card--back { left: 630px; }

  .brand {
    position: absolute;
    left: 0; right: 0;
    display: flex;
    flex-direction: column;
    align-items: center;
  }
  .brand__mark {
    width: 40px; height: 40px;
    border-radius: 50%;
    background: var(--band-green);
  }
  .brand__name {
    font-family: "Cinzel", "Times New Roman", serif;
    font-weight: 400;
    color: var(--brand-blue);
    letter-spacing: 1px;
    white-space: nowrap;
  }
  .card--front .brand { top: 26px; }
  .card--front .brand__name { font-size: 25px; margin-top: 8px; line-height: 1.1; }
  .brand__tagline {
    font-family: "Cinzel", "Times New Roman", serif;
    font-size: 8px;
    letter-spacing: 1px;
    color: var(--text-muted);
    margin-top: 3px;
    white-space: nowrap;
  }

  .band-name {
    position: absolute;
    left: 0; right: 0; top: 132px; height: 32px;
    background: linear-gradient(90deg, var(--band-green-dark), var(--band-green) 50%, var(--band-green-dark));
    display: flex; align-items: center; justify-content: center;
    color: var(--text-light);
    font-weight: 700; font-size: 15px; letter-spacing: 1px;
  }
  .band-contact {
    position: absolute;
    left: 0; right: 0; top: 164px; height: 72px;
    background: linear-gradient(180deg, var(--band-blue) 0%, var(--band-blue-dark) 60%, rgba(5,5,5,0) 100%);
    display: flex; flex-direction: column; align-items: center;
    padding-top: 12px; gap: 12px;
    color: var(--text-light);
    font-size: 11px;
  }
  .contact-row { display: flex; gap: 26px; }
  .contact-item { display: flex; align-items: center; gap: 5px; white-space: nowrap; }
  .contact-item svg { width: 11px; height: 11px; fill: var(--text-light); }
  .address { white-space: nowrap; }

  .card--back .brand { top: 80px; }
  .card--back .brand__mark { width: 70px; height: 70px; }
  .card--back .brand__name { font-size: 22px; margin-top: 12px; }
  .website {
    position: absolute;
    left: 0; right: 0; top: 256px;
    text-align: center;
    font-family: "Cinzel", "Times New Roman", serif;
    font-size: 15px;
    letter-spacing: 3px;
    color: var(--text-light);
    white-space: nowrap;
  }
</style>
</head>
<body>
  <section class="card card--front" aria-label="Business card front">
    <div class="brand">
      <span class="brand__mark"></span>
      <div class="brand__name">Brightvale Marks</div>
      <div class="brand__tagline">CLEAR IDEAS FOR LASTING GROWTH</div>
    </div>
    <div class="band-name">KEMI VARO</div>
    <div class="band-contact">
      <div class="contact-row">
        <span class="contact-item">
          <svg viewBox="0 0 24 24" aria-hidden="true"><path d="M6.6 10.8a15.1 15.1 0 0 0 6.6 6.6l2.2-2.2a1 1 0 0 1 1-.25 11.4 11.4 0 0 0 3.6.57 1 1 0 0 1 1 1V20a1 1 0 0 1-1 1A17 17 0 0 1 3 4a1 1 0 0 1 1-1h3.5a1 1 0 0 1 1 1c0 1.25.2 2.45.57 3.6a1 1 0 0 1-.25 1z"/></svg>
          08140005172
        </span>
        <span class="contact-item">
          <svg viewBox="0 0 24 24" aria-hidden="true"><path d="M2 5h20v14H2zm2 2v.5l8 5 8-5V7l-8 5z"/></svg>
          info@brightvalemarks.com
        </span>
      </div>
      <div class="address">47 Olumide Bankole Crescent, Wuse 2, Abuja, Nigeria</div>
    </div>
  </section>

  <section class="card card--back" aria-label="Business card back">
    <div class="brand">
      <span class="brand__mark"></span>
      <div class="brand__name">Brightvale Marks</div>
    </div>
    <div class="website">WWW.BRIGHTVALEMARKS.COM</div>
  </section>
</body>
</html>
```